New locally owned rental company needs a flyer to circulate

Need flyer with logo, phone# and address. We rent cars to anyone with driver's license and proper insurance. Rates as low as $50/day. Can offer compact cars, mid-size and full size sedans. Also SUV's.

```html
<!DOCTYPE html>
<html lang="en">
<head>
<meta charset="utf-8">
<title>DriveLane Car &amp; Van Rental Flyer</title>
<link rel="stylesheet" href="https://fonts.googleapis.com/css2?family=Jost:wght@500;600;700;800&display=swap">
<style>
  :root {
    --stage: #e6e6e6;
    --blue: #0d4a9f;
    --green: #23a13e;
    --black: #121212;
    --white: #ffffff;
    --ink-dark: #14201a;
    --photo-lot-a: #2a5bb8;
    --photo-lot-b: #3f73c9;
    --photo-car-a: #c81e2a;
    --photo-car-b: #7d1016;
  }
  * { margin: 0; padding: 0; box-sizing: border-box; }
  html, body { width: 1200px; height: 1200px; overflow: hidden; }
  body {
    background: var(--stage);
    font-family: "Jost", "Futura", sans-serif;
    display: flex; align-items: center; justify-content: center;
  }
  .flyer {
    position: relative;
    width: 880px; height: 1140px;
    background: var(--blue);
    overflow: hidden;
    color: var(--white);
  }
  .flyer__shapes { position: absolute; inset: 0; width: 100%; height: 100%; }
  .lot-photo {
    position: absolute; left: 0; top: 0; width: 880px; height: 170px;
    background: linear-gradient(180deg, var(--photo-lot-b) 0%, var(--photo-lot-a) 70%, var(--blue) 100%);
  }
  .headline {
    position: absolute; top: 168px; left: 0; width: 100%;
    text-align: center; text-transform: uppercase;
  }
  .headline__main { font-size: 96px; font-weight: 800; letter-spacing: 2px; line-height: 1; }
  .headline__sub { font-size: 36px; font-weight: 700; line-height: 1.15; letter-spacing: 1px; margin-top: 6px; }
  .highlight { background: var(--green); padding: 0 8px; }
  .rate { position: absolute; left: 60px; top: 400px; text-transform: uppercase; }
  .rate__label {
    display: inline-block; background: var(--black);
    font-size: 26px; font-weight: 700; padding: 6px 22px; letter-spacing: .5px;
  }
  .rate__price {
    display: block; width: max-content; margin-left: 50px; background: var(--green);
    font-size: 58px; font-weight: 800; padding: 2px 22px; line-height: 1.1;
  }
  .car-photo {
    position: absolute; left: 70px; top: 545px; width: 760px; height: 240px;
    border-radius: 46% 40% 18% 22% / 60% 50% 22% 30%;
    background: radial-gradient(ellipse at 45% 45%, var(--photo-car-a) 0%, var(--photo-car-b) 80%);
  }
  .brand { position: absolute; right: 70px; top: 792px; text-align: center; }
  .brand__name { font-size: 70px; font-weight: 800; line-height: .95; letter-spacing: -1px; }
  .brand__tag { font-size: 24px; font-weight: 600; letter-spacing: 9px; }
  .offer-band {
    position: absolute; left: 40px; right: 0; top: 900px; height: 54px;
    background: var(--black);
    clip-path: polygon(22px 0, 100% 0, 100% 100%, 0 100%);
    display: flex; align-items: center; justify-content: center;
    padding-left: 24px;
    font-size: 19px; font-weight: 700; text-transform: uppercase;
    white-space: nowrap;
  }
  .contact { position: absolute; text-transform: uppercase; }
  .contact__label { color: var(--ink-dark); font-size: 26px; font-weight: 800; line-height: 1.3; }
  .contact--phone { left: 60px; top: 1038px; }
  .contact--phone .contact__value { font-size: 60px; font-weight: 700; line-height: 1; }
  .contact--address { left: 470px; top: 966px; }
  .contact--address .contact__value { font-size: 21px; font-weight: 700; line-height: 1.2; white-space: nowrap; }
</style>
</head>
<body>
  <main class="flyer">
    <svg class="flyer__shapes" viewBox="0 0 880 1140" aria-hidden="true">
      <polygon points="0,790 880,300 880,650 700,1140 0,1140" fill="var(--green)"/>
    </svg>

    <div class="lot-photo" role="img" aria-label="Photo of rental cars parked in a row in front of the office"></div>

    <header class="headline">
      <h1 class="headline__main">We Rent Cars</h1>
      <p class="headline__sub">To anyone with <span class="highlight">Driver's License</span><br>and <span class="highlight">Proper Insurance</span></p>
    </header>

    <div class="rate">
      <span class="rate__label">Rates as low as</span>
      <span class="rate__price">$50/Day</span>
    </div>

    <div class="car-photo" role="img" aria-label="Photo of a red compact sedan with a Rent Me sign on the windshield"></div>

    <div class="brand">
      <div class="brand__name">DriveLane</div>
      <div class="brand__tag">Car &amp; Van Rental</div>
    </div>

    <div class="offer-band">Can offer | Compact cars | Mid-size | Full size sedans | SUV's</div>

    <div class="contact contact--address">
      <div class="contact__label">Address</div>
      <div class="contact__value">4870B South Harbor Boulevard<br>Maplewood, AL 35899</div>
    </div>

    <div class="contact contact--phone">
      <div class="contact__label">Phone</div>
      <div class="contact__value">256-555-0142</div>
    </div>
  </main>
</body>
</html>
```